Water ATM Card

Need a design for water ATM cards. Size of card is 3.375 x 2.125 inch
On the Front include the Cedar brook Logo.
Bottom right corner should have Price $100
On the Back
This card is to be used to access water refills at any Cedar Brook Water Vending Machines.
Please contact (869) 614 2938 or (869) 731 4072 or email clearflowhq@examplemail.com for any assistance or recharging of card.

```html
<!DOCTYPE html>
<html lang="en">
<head>
<meta charset="utf-8">
<title>Cedar Brook Water Card</title>
<link href="https://fonts.googleapis.com/css2?family=Lato:ital,wght@0,300;0,400;0,700;0,900;1,400&display=swap" rel="stylesheet">
<style>
  :root {
    --board: #bdbdbd;
    --label: #5a5a5a;
    --card-white: #ffffff;
    --brand-blue: #1a6fbf;
    --wave-blue: #1466bd;
    --wave-navy: #27358f;
    --wave-green: #4caf3f;
    --back-top: #283f96;
    --back-mid: #1558b4;
    --back-bottom: #1a6cc0;
    --back-edge: #0d2a6a;
    --text-light: #ffffff;
  }
  * { margin: 0; padding: 0; box-sizing: border-box; }
  html, body { width: 1200px; height: 1000px; overflow: hidden; }
  body {
    background: var(--board);
    font-family: "Lato", sans-serif;
    position: relative;
  }
  .side-label {
    position: absolute;
    left: 263px;
    font-family: "Lato", sans-serif;
    font-weight: 300;
    font-size: 26px;
    letter-spacing: 8px;
    color: var(--label);
    transform: translate(-50%, -50%) rotate(-90deg);
    white-space: nowrap;
  }
  .side-label--front { top: 318px; }
  .side-label--back { top: 710px; }

  .card {
    position: absolute;
    left: 347px;
    width: 506px;
    height: 319px;
    border-radius: 28px;
    overflow: hidden;
    box-shadow: 0 3px 8px rgba(0,0,0,0.28);
  }
  .card--front { top: 158px; background: var(--card-white); }
  .card--back {
    top: 551px;
    background:
      linear-gradient(90deg, rgba(0,0,0,0) 70%, var(--back-edge) 100%),
      linear-gradient(180deg, var(--back-top) 0%, var(--back-mid) 55%, var(--back-bottom) 100%);
  }

  .brand {
    position: absolute;
    left: 0;
    width: 100%;
    top: 156px;
    text-align: center;
    color: var(--brand-blue);
    padding-right: 12px;
  }
  .brand__name {
    font-weight: 700;
    font-size: 27px;
    letter-spacing: 0.5px;
    line-height: 1;
  }
  .brand__tagline {
    font-weight: 400;
    font-size: 18px;
    line-height: 1;
    margin-top: 3px;
  }

  .price-swoosh { position: absolute; left: 0; top: 0; }
  .price {
    position: absolute;
    right: 16px;
    bottom: 14px;
    text-align: right;
    color: var(--text-light);
  }
  .price__label {
    font-style: italic;
    font-size: 18px;
    line-height: 1;
    margin-right: 6px;
  }
  .price__amount {
    font-weight: 700;
    font-size: 40px;
    line-height: 1.05;
  }

  .splash-photo {
    position: absolute;
    left: 0;
    top: 0;
    width: 100%;
    height: 205px;
    background:
      radial-gradient(ellipse 60% 30% at 55% 60%, rgba(120,170,230,0.35), rgba(0,0,0,0) 70%),
      linear-gradient(180deg, rgba(40,63,150,0) 0%, rgba(30,80,170,0.5) 60%, rgba(26,108,192,0) 100%);
  }
  .card-terms {
    position: absolute;
    left: 0;
    width: 100%;
    top: 215px;
    text-align: center;
    color: var(--text-light);
    font-size: 13.5px;
    line-height: 19px;
  }
</style>
</head>
<body>
  <div class="side-label side-label--front">FRONT</div>
  <div class="side-label side-label--back">BACK</div>

  <section class="card card--front">
    <div class="brand">
      <div class="brand__name">CEDAR BROOK</div>
      <div class="brand__tagline">Purified Spring Water</div>
    </div>
    <svg class="price-swoosh" width="506" height="319" viewBox="0 0 506 319" aria-hidden="true">
      <path d="M292 319 C360 290 380 205 506 207 L506 319 Z" fill="var(--wave-blue)"/>
      <path d="M292 319 C360 288 378 206 506 207" fill="none" stroke="var(--card-white)" stroke-width="5"/>
      <path d="M290 314 C350 282 365 205 470 201 C485 200 496 201 506 202" fill="none" stroke="var(--wave-navy)" stroke-width="6"/>
      <path d="M292 312 C345 275 360 207 460 203" fill="none" stroke="var(--wave-green)" stroke-width="3"/>
    </svg>
    <div class="price">
      <div class="price__label">Price</div>
      <div class="price__amount">$100</div>
    </div>
  </section>

  <section class="card card--back">
    <div class="splash-photo" role="img" aria-label="Photo of blue water splashing with droplets"></div>
    <p class="card-terms">
      This card is to be used to access water refills at any<br>
      Cedar Brook Water Vending Machines. Please contact (869) 614 2938<br>
      or (869) 731 4072 or email clearflowhq@examplemail.com for any assistance<br>
      or recharging of card.
    </p>
  </section>
</body>
</html>
```